Kelpa Stride - Graphic Label

Company Name: Verdant Pillar
Product: Organic Energy Drink
Name of Drink : Kelpa Stride
8.45oz - Bottle
http://www.tradobin-example.com/item-view/Metal-drink-bottle-sample_4928061735.html?r=q
Attached will be examples of labels for other drinks associated with this company along with company logo. I'm open to all interpretations of design. Please submit creative ideas and we can adjust design as we go.
Design must have some integration of the geometry as seen in labels attached.
Keep it classy
If you have a vision for the design, just create it and we can adjust from there.
I want the bottle to have long lasting but creative/interesting design..
Reason: Design sought has not been submited, the deadline has been extended.
Please continue submissions.
- Thanks
Target Market(s)
All Ages .. those interested in Organics, health drinks, energy drinks
Industry/Entity Type
It Company

```html
<!DOCTYPE html>
<html lang="en">
<head>
<meta charset="utf-8">
<title>Kelpa Stride – Label</title>
<link rel="stylesheet" href="https://fonts.googleapis.com/css2?family=Fredoka:wght@500;600&family=Roboto+Slab:wght@700;800&family=Kaushan+Script&display=swap">
<style>
  :root{
    --page:#f3f2f5;
    --label-deep:#3e1468;
    --label-mid:#5a1f8f;
    --label-light:#7a3bb3;
    --ink-light:#ffffff;
    --art-top:#4a1f6e;
    --art-bottom:#2e0f47;
    --badge-fill:#ffffff;
    --badge-ink:#3e1468;
  }
  *{margin:0;padding:0;box-sizing:border-box}
  html,body{width:1012px;height:1200px;overflow:hidden;background:var(--page)}
  .canvas{position:relative;width:1012px;height:1200px;display:flex;align-items:center;justify-content:center}
  .label{
    position:relative;width:560px;height:1060px;border-radius:18px;overflow:hidden;
    background:linear-gradient(180deg,var(--label-deep) 0%,var(--label-mid) 45%,var(--label-light) 62%,var(--label-mid) 80%,var(--label-deep) 100%);
    display:flex;flex-direction:column;align-items:center;color:var(--ink-light);
  }
  .label__geometry{position:absolute;inset:0;
    background:radial-gradient(ellipse at 50% 52%,rgba(255,255,255,.14),rgba(255,255,255,0) 60%);}
  .brand{position:relative;margin-top:70px;display:flex;align-items:center;gap:10px;
    font-family:"Roboto Slab",serif;font-weight:700;font-size:20px;letter-spacing:.5px}
  .brand__dot{width:16px;height:16px;border-radius:50%;background:var(--ink-light)}
  .title{position:relative;margin-top:130px;text-align:center;line-height:1}
  .title__main{display:block;font-family:"Fredoka",sans-serif;font-weight:600;font-size:128px;letter-spacing:2px}
  .title__sub{display:block;margin-top:18px;font-family:"Roboto Slab",serif;font-weight:800;font-size:46px;letter-spacing:6px}
  .art{position:relative;margin-top:30px;width:260px;height:150px;border-radius:12px;
    background:linear-gradient(180deg,var(--art-top),var(--art-bottom));}
  .tagline{position:relative;margin-top:40px;font-family:"Kaushan Script",cursive;font-size:40px}
  .badges{position:relative;margin-top:60px;display:flex;gap:18px;list-style:none}
  .badge{position:relative;width:92px;height:82px;display:flex;align-items:center;justify-content:center;text-align:center;
    font-family:"Roboto Slab",serif;font-weight:700;font-size:17px;line-height:1.15;color:var(--badge-ink)}
  .badge svg{position:absolute;inset:0}
  .badge span{position:relative}
  .cert{position:relative;margin-top:60px;width:58px;height:58px;border-radius:50%;background:var(--badge-fill)}
  .volume{position:relative;margin-top:12px;font-family:"Roboto Slab",serif;font-weight:700;font-size:26px}
</style>
</head>
<body>
<main class="canvas">
  <section class="label">
    <div class="label__geometry" role="img" aria-label="Faint hexagon geometry pattern across the label"></div>

    <div class="brand"><span class="brand__dot"></span>Verdant Pillar</div>

    <h1 class="title">
      <span class="title__main">kelpa</span>
      <span class="title__sub">STRIDE</span>
    </h1>

    <div class="art" role="img" aria-label="Illustration area: dark purple berries with green leaves"></div>

    <p class="tagline">Organic Energy</p>

    <ul class="badges">
      <li class="badge">
        <svg viewBox="0 0 92 82" width="92" height="82"><polygon points="23,2 69,2 90,41 69,80 23,80 2,41" fill="#fff"/></svg>
        <span>100%<br>Juice</span>
      </li>
      <li class="badge">
        <svg viewBox="0 0 92 82" width="92" height="82"><polygon points="23,2 69,2 90,41 69,80 23,80 2,41" fill="#fff"/></svg>
        <span>No<br>GMO</span>
      </li>
      <li class="badge">
        <svg viewBox="0 0 92 82" width="92" height="82"><polygon points="23,2 69,2 90,41 69,80 23,80 2,41" fill="#fff"/></svg>
        <span>100%<br>Vegan</span>
      </li>
    </ul>

    <div class="cert" role="img" aria-label="Organic certification seal"></div>
    <p class="volume">230 ml</p>
  </section>
</main>
</body>
</html>
```